Kivora - a fintech company - business card

We need a business card design for our Payments Technology company in Sydney, Australia. We provide business with payment solutions expanding across EFTPOS machines, online payment gateways and mobile payment solutions. We would like to see designs that are clean, classy and professional.
Target Market(s)
Business professionals, executives, c-suite
Industry/Entity Type
Fintech
Contact Information for Business Card
Will be on 400gsm. Logo will most likely be spot gloss unless designer recommends otherwise.
Font styles to use
Sans Serif
Requirements
Must have
- We need our website (kivora.com.au), email (contact@kivora.com.au), mobile (0455 806 274) and direct phone number (02 7391 5082) to feature on the card along with our logo (attached) and the words "EFTPOS | ONLINE | MOBILE"
- Font = Roboto

```html
<!DOCTYPE html>
<html lang="en">
<head>
<meta charset="utf-8">
<title>Kivora – Business Card</title>
<link href="https://fonts.googleapis.com/css2?family=Roboto:wght@400;500;700;900&display=swap" rel="stylesheet">
<style>
  :root {
    --brand-blue: #1f6496;
    --ink-grey: #666a6e;
    --paper: #ffffff;
    --backdrop: #3a3c3f;
    --rule: #6f9cc0;
  }
  * { box-sizing: border-box; margin: 0; padding: 0; }
  html, body {
    width: 1200px; height: 900px; overflow: hidden;
    background: var(--backdrop);
    font-family: "Roboto", sans-serif;
  }
  .stage {
    position: relative; width: 1200px; height: 900px;
  }
  .card {
    position: absolute; left: 290px; width: 620px; height: 376px;
    border-radius: 26px; overflow: hidden;
    box-shadow: 0 14px 30px rgba(0,0,0,0.45);
  }

  /* Front */
  .card--front { top: 56px; background: var(--brand-blue); color: var(--paper); }
  .front-brand {
    position: absolute; left: 0; right: 0; top: 118px;
    display: flex; align-items: center; justify-content: center; gap: 20px;
  }
  .front-brand .brand-dot { width: 56px; height: 56px; border-radius: 50%; background: var(--paper); }
  .front-brand .brand-name { font-weight: 900; font-size: 64px; letter-spacing: 1px; }
  .services {
    position: absolute; left: 0; right: 0; top: 236px;
    text-align: center; font-weight: 500; font-size: 17px; letter-spacing: 1.5px;
  }
  .services .divider { margin: 0 18px; font-weight: 400; }

  /* Back */
  .card--back { top: 468px; background: var(--paper); }
  .back-brand {
    position: absolute; left: 46px; top: 56px;
    display: flex; align-items: center; gap: 14px;
  }
  .back-brand .brand-dot { width: 46px; height: 46px; border-radius: 50%; background: var(--brand-blue); }
  .back-brand .brand-name { font-weight: 900; font-size: 44px; color: var(--ink-grey); letter-spacing: 0.5px; }
  .holder {
    position: absolute; right: 48px; top: 64px; text-align: right;
  }
  .holder .holder-name { font-weight: 700; font-size: 30px; color: var(--brand-blue); }
  .holder .holder-title { font-weight: 500; font-size: 17px; color: var(--ink-grey); margin-top: 4px; }
  .accent-tab {
    position: absolute; right: 0; top: 62px; width: 24px; height: 64px; background: var(--brand-blue);
  }
  .divider-rule {
    position: absolute; left: 46px; right: 48px; top: 150px; height: 1px; background: var(--rule);
  }
  .contacts {
    position: absolute; left: 46px; top: 168px; list-style: none;
    font-size: 16px; line-height: 29px; color: var(--ink-grey);
  }
  .contacts .label { color: var(--brand-blue); font-weight: 500; margin-right: 4px; }
  .base-band {
    position: absolute; left: 0; right: 0; bottom: 0; height: 16px; background: var(--brand-blue);
  }
</style>
</head>
<body>
  <main class="stage">
    <section class="card card--front" aria-label="Card front">
      <div class="front-brand">
        <span class="brand-dot"></span>
        <span class="brand-name">KIVORA</span>
      </div>
      <p class="services">EFTPOS<span class="divider">|</span>ONLINE<span class="divider">|</span>MOBILE</p>
    </section>

    <section class="card card--back" aria-label="Card back">
      <div class="back-brand">
        <span class="brand-dot"></span>
        <span class="brand-name">KIVORA</span>
      </div>
      <div class="accent-tab"></div>
      <div class="holder">
        <p class="holder-name">Elias Hart</p>
        <p class="holder-title">General Manager</p>
      </div>
      <div class="divider-rule"></div>
      <ul class="contacts">
        <li><span class="label">P:</span>02 7391 5082</li>
        <li><span class="label">Mo:</span>0455 806 274</li>
        <li><span class="label">M:</span>contact@kivora.com.au</li>
        <li><span class="label">E:</span>kivora.com.au</li>
        <li><span class="label">L:</span>Harbour Lane, Westmere Park, 2040</li>
      </ul>
      <div class="base-band"></div>
    </section>
  </main>
</body>
</html>
```